Brennwald Metrics GmbH
Brennwald Metrics GmbH - Financial Services
Creative Brief
Professional
Lionel T Brennwald
Managing Director
Lindenweg 42 CH-6300 Zug Switzerland
U.S. Telephone 203.555.0186
lionel.brennwald@brennwaldmetrics-example.ch
brennwaldmetrics-example.ch
Wedsite will have partial moon crater stripped across the top. It might be interesting on the business card. Hard to tell if it will be too busy. JPG attached. Else simple is better. Note that address is broken after 19, and after Zug. It doesn't show on the confirmation. Kindly upload business cards and stationary, not just Business cards. It has to be a package

```html
<!DOCTYPE html>
<html lang="en">
<head>
<meta charset="utf-8">
<title>Brennwald Metrics GmbH – Stationery Package</title>
<link href="https://fonts.googleapis.com/css2?family=Open+Sans:wght@400;600;700&display=swap" rel="stylesheet">
<style>
:root{
  --navy:#1b3a72;
  --blue:#2b62ae;
  --sky:#5d8fd0;
  --paper:#ffffff;
  --ground:#ebebea;
  --ink:#3a3f48;
  --muted:#8a9099;
  --rule:#c9ccd2;
  --moon-dark:#5d5f5c;
  --moon-mid:#9a9b94;
  --moon-light:#d2d2cb;
}
*{box-sizing:border-box;margin:0;padding:0}
html,body{width:1200px;height:545px;overflow:hidden}
body{background:var(--ground);font-family:"Open Sans",Arial,sans-serif;color:var(--ink);position:relative}
.sheet{position:absolute;background:var(--paper);box-shadow:0 2px 6px rgba(0,0,0,.18);overflow:hidden}
.moon-band{position:absolute;background:linear-gradient(100deg,var(--moon-mid) 0%,var(--moon-light) 22%,var(--moon-dark) 45%,var(--moon-mid) 65%,var(--moon-light) 82%,var(--moon-dark) 100%)}
.brand{position:absolute;background:var(--navy);color:#fff;display:flex;align-items:center;gap:5px;padding:0 6px;font-weight:600;letter-spacing:.06em;line-height:1.05}
.brand .mark{width:9px;height:9px;background:#fff;flex:none}
.brand .name{font-size:7px}
.small{font-size:4.5px;line-height:1.45;color:var(--muted)}

/* business cards */
.card-front{left:24px;top:24px;width:136px;height:78px}
.card-front .brand{left:8px;top:8px;height:22px}
.card-front .who{position:absolute;left:8px;top:40px;font-size:5px;color:var(--ink)}
.card-front .who b{font-weight:600;display:block}
.card-front .contact{position:absolute;right:8px;top:40px;text-align:right}
.card-back{left:166px;top:24px;width:248px;height:86px}
.card-back .moon-band{inset:0}
.card-back .brand{left:88px;top:32px;height:24px}

/* envelope front */
.env-front{left:24px;top:156px;width:390px;height:196px}
.env-front .moon-band{left:0;right:0;top:12px;height:36px}
.env-front .brand{left:0;top:12px;height:36px;padding:0 10px}
.env-front .addr{position:absolute;left:14px;bottom:22px}
.env-front .contact{position:absolute;left:196px;bottom:22px}

/* envelope back */
.env-back{left:24px;top:360px;width:390px;height:178px;background:#f4f5f7}
.env-back svg{position:absolute;inset:0}
.env-back .brand{left:163px;top:14px;height:22px;background:transparent}

/* letterhead */
.letter{left:432px;top:12px;width:372px;height:526px}
.letter .moon-band{left:0;right:0;top:12px;height:48px}
.letter .brand{left:0;top:12px;height:48px;padding:0 12px}
.letter .body{position:absolute;left:44px;right:44px;top:92px;font-size:5px;line-height:1.6;color:var(--ink)}
.letter .body p{margin-bottom:9px}
.letter .footer{position:absolute;left:44px;right:44px;bottom:20px;display:flex;justify-content:space-between;color:var(--blue)}

/* fax */
.fax{left:823px;top:12px;width:369px;height:526px}
.fax .moon-band{left:0;right:0;top:12px;height:48px}
.fax .brand{left:0;top:12px;height:48px;padding:0 12px}
.fax-bar{position:absolute;left:14px;right:14px;top:138px;height:18px;background:linear-gradient(90deg,var(--navy),var(--blue) 70%,var(--sky));color:#fff;font-weight:700;font-size:8px;display:flex;align-items:center;justify-content:flex-end;gap:5px;padding-right:12px;letter-spacing:.1em}
.fax-panel{position:absolute;left:14px;right:14px;top:156px;height:300px;border:1px solid var(--rule);border-top:0}
.tag{position:absolute;left:18px;width:28px;height:11px;background:var(--navy);color:#fff;font-size:4.5px;font-weight:600;display:flex;align-items:center;justify-content:center;letter-spacing:.05em}
.field{position:absolute;left:96px;width:145px;height:12px;border-bottom:1px solid var(--rule);font-size:4.5px;color:var(--muted);padding-top:3px}
.field span{display:inline-block;width:36px}
.notes-box{position:absolute;left:96px;right:18px;top:148px;height:132px;border:1px solid var(--rule)}
.fax .footer{position:absolute;left:30px;right:30px;bottom:20px;display:flex;justify-content:space-between;color:var(--blue)}
</style>
</head>
<body>

<!-- business card: details side -->
<section class="sheet card-front" aria-label="Business card, details side">
  <div class="brand"><span class="mark"></span><span class="name">BRENNWALD<br>METRICS</span></div>
  <div class="who"><b>Lionel T Brennwald</b><span class="small">Managing Director</span></div>
  <div class="contact small">Lindenweg 42<br>CH-6300 Zug<br>Switzerland<br>203.555.0186<br>brennwaldmetrics-example.ch</div>
</section>

<!-- business card: image side -->
<section class="sheet card-back" aria-label="Business card, image side">
  <div class="moon-band" role="img" aria-label="Photograph of a cratered lunar surface"></div>
  <div class="brand"><span class="mark"></span><span class="name">BRENNWALD<br>METRICS</span></div>
</section>

<!-- envelope front -->
<section class="sheet env-front" aria-label="Envelope front">
  <div class="moon-band" role="img" aria-label="Strip of cratered lunar surface"></div>
  <div class="brand"><span class="mark"></span><span class="name">BRENNWALD<br>METRICS</span></div>
  <div class="addr small">Brennwald Metrics GmbH<br>Lindenweg 42<br>CH-6300 Zug<br>Switzerland</div>
  <div class="contact small">U.S. Telephone 203.555.0186<br>lionel.brennwald@brennwaldmetrics-example.ch<br>brennwaldmetrics-example.ch</div>
</section>

<!-- envelope back -->
<section class="sheet env-back" aria-label="Envelope back">
  <svg width="390" height="178" viewBox="0 0 390 178" aria-hidden="true">
    <defs>
      <linearGradient id="flap-fill" x1="0" y1="0" x2="0" y2="1">
        <stop offset="0" stop-color="#1b3a72"/>
        <stop offset="1" stop-color="#5d8fd0"/>
      </linearGradient>
    </defs>
    <path d="M0 178 L170 92 L220 92 L390 178" fill="none" stroke="#c9ccd2" stroke-width="1"/>
    <path d="M0 0 H390 V22 L195 80 L0 22 Z" fill="url(#flap-fill)"/>
  </svg>
  <div class="brand"><span class="mark"></span><span class="name">BRENNWALD<br>METRICS</span></div>
</section>

<!-- letterhead -->
<section class="sheet letter" aria-label="Letterhead">
  <div class="moon-band" role="img" aria-label="Strip of cratered lunar surface"></div>
  <div class="brand"><span class="mark"></span><span class="name">BRENNWALD<br>METRICS</span></div>
  <div class="body">
    <p>12 March 2024</p>
    <p>Jonas Keller<br>Seestrasse 8<br>8002 Zurich</p>
    <p>Dear Mr Keller,</p>
    <p>Thank you for your interest in our services. This letter confirms the scope we discussed and outlines the next steps for the quarterly review of your portfolio and reporting needs.</p>
    <p>Our team will prepare a detailed analysis of current positions, risk measures and performance data. We will share the first draft within two weeks and schedule a call to review the findings together.</p>
    <p>Please let us know if you have any questions in the meantime.</p>
    <p>Regards,<br><br>Lionel T Brennwald</p>
  </div>
  <div class="footer small"><span>Brennwald Metrics GmbH<br>Lindenweg 42 CH-6300 Zug Switzerland</span><span>203.555.0186<br>brennwaldmetrics-example.ch</span></div>
</section>

<!-- fax cover -->
<section class="sheet fax" aria-label="Fax cover sheet">
  <div class="moon-band" role="img" aria-label="Strip of cratered lunar surface"></div>
  <div class="brand"><span class="mark"></span><span class="name">BRENNWALD<br>METRICS</span></div>
  <div class="fax-bar">
    <svg width="12" height="8" viewBox="0 0 12 8" aria-hidden="true"><path d="M0 4H10M7 1L10 4L7 7" stroke="#fff" stroke-width="1.4" fill="none"/></svg>FAX
  </div>
  <div class="fax-panel">
    <div class="tag" style="top:10px">TO</div>
    <div class="field" style="top:6px"><span>To</span></div>
    <div class="field" style="top:22px"><span>From</span></div>
    <div class="field" style="top:38px"><span>Company</span></div>
    <div class="field" style="top:54px"><span>Fax</span></div>
    <div class="field" style="top:70px"><span>Phone</span></div>
    <div class="tag" style="top:98px">FROM</div>
    <div class="field" style="top:94px"><span>Date</span></div>
    <div class="field" style="top:110px"><span>Pages</span></div>
    <div class="field" style="top:126px"><span>Re</span></div>
    <div class="tag" style="top:150px">NOTES</div>
    <div class="notes-box"></div>
  </div>
  <div class="footer small"><span>Brennwald Metrics GmbH<br>Lindenweg 42 CH-6300 Zug Switzerland</span><span>203.555.0186<br>brennwaldmetrics-example.ch</span></div>
</section>

</body>
</html>
```